Black Friday for Baby Boutique

I need a flyer for my Black Friday and Local Goods Sunday events.

Entire store will be 30% off.

Friday hours: 9-6
Saturday: 9-4

Each customer will receive a coupon for December 1-24.

First 25 customers each day will receive a surprise gift valued at $50+

TONS of giveaways, food & drinks!

Bring/Buy an unopened toy for Marshgate Kin Aid & receive a $10 gift card.

Velvet Cradle
Bluffton, SC
Oakridge Plaza : Next to Pine Grill
(555) 214-7093

```html
<!DOCTYPE html>
<html lang="en">
<head>
<meta charset="utf-8">
<title>Velvet Cradle – Holiday Sale Flyer</title>
<link href="https://fonts.googleapis.com/css2?family=Bebas+Neue&family=Montserrat:wght@600;700&family=Oswald:wght@500&display=swap" rel="stylesheet">
<style>
  :root {
    --page-bg: #ecebea;
    --mint-top: #b7dcd1;
    --mint-bottom: #d6ebe4;
    --ink: #263330;
    --ink-soft: #3b4644;
    --ribbon: #d8242c;
    --pine: #1c6a54;
    --pine-dark: #124a3b;
    --snow: #ffffff;
    --mist: #e9edf0;
    --tree-grey: #b3b6c4;
    --contact-green: #1a6650;
  }
  * { margin: 0; padding: 0; box-sizing: border-box; }
  html, body {
    width: 1200px; height: 1200px; overflow: hidden;
    background: var(--page-bg);
  }
  .flyer {
    position: absolute; left: 175px; top: 0;
    width: 850px; height: 1200px;
    overflow: hidden;
    background: var(--mist);
    font-family: "Bebas Neue", "Oswald", sans-serif;
    color: var(--ink);
  }
  .sale-header {
    position: absolute; left: 0; top: 0; width: 100%; height: 469px;
    background: radial-gradient(ellipse at 50% 30%, var(--mint-bottom) 0%, var(--mint-top) 80%);
  }
  .centered { position: absolute; left: 0; width: 100%; text-align: center; }
  .headline-lead { top: 92px; font-size: 96px; line-height: 1; letter-spacing: 0.5px; font-weight: 400; }
  .headline-discount { top: 184px; font-size: 122px; line-height: 1; }
  .hours-band {
    position: absolute; left: 130px; top: 305px; width: 590px; height: 53px;
    background: var(--ribbon);
  }
  .hours-text {
    top: 309px; font-size: 46px; line-height: 1; color: var(--snow);
    letter-spacing: 0.5px; word-spacing: 2px;
  }
  .coupon-note {
    top: 392px; font-family: "Montserrat", sans-serif; font-weight: 700;
    font-size: 28px; line-height: 36px; letter-spacing: 1px; color: var(--ink-soft);
  }
  .early-bird {
    position: absolute; left: 0; top: 469px; width: 100%; height: 126px;
    background: linear-gradient(90deg, var(--pine-dark) 0%, var(--pine) 50%, var(--pine-dark) 100%);
    color: var(--snow); text-align: center;
  }
  .early-bird-title { display: block; padding-top: 12px; font-size: 66px; line-height: 62px; }
  .early-bird-sub { display: block; font-size: 44px; line-height: 40px; }
  .winter-scene {
    position: absolute; left: 0; top: 760px; width: 100%; height: 440px;
    background: linear-gradient(to bottom, rgba(179,182,196,0) 0%, var(--tree-grey) 30%, var(--tree-grey) 52%, var(--snow) 72%, var(--snow) 100%);
  }
  .gift-boxes {
    position: absolute; left: 24px; top: 794px; width: 453px; height: 400px;
    background: radial-gradient(ellipse at 50% 60%, #d9323a 0%, #e9a9ad 45%, rgba(255,255,255,0) 75%);
  }
  .perks {
    top: 612px; font-size: 38px; line-height: 48px; letter-spacing: 1.5px; color: var(--ink-soft);
  }
  .shop-info {
    position: absolute; left: 490px; top: 970px; width: 330px; text-align: center;
    font-family: "Oswald", sans-serif; font-weight: 500; font-style: normal; color: var(--ink-soft);
    font-size: 21px; line-height: 31px;
  }
  .shop-phone {
    display: block; margin-top: 4px;
    font-family: "Bebas Neue", sans-serif; font-size: 48px; line-height: 50px;
    color: var(--contact-green); letter-spacing: 1px;
  }
  .social-row { display: flex; justify-content: center; gap: 24px; margin-top: 16px; }
  .social-dot { width: 32px; height: 32px; border-radius: 50%; background: var(--ink-soft); }
</style>
</head>
<body>
  <main class="flyer">
    <section class="sale-header">
      <h1 class="centered headline-lead">Entire Store Will Be</h1>
      <p class="centered headline-discount">30% Off</p>
      <div class="hours-band" role="img" aria-label="Red ribbon banner"></div>
      <p class="centered hours-text">Friday Hours: 9-6 &nbsp;|&nbsp; Saturday: 9-4</p>
      <p class="centered coupon-note">Each customer will receive a<br>coupon for December 1-24.</p>
    </section>

    <section class="early-bird">
      <span class="early-bird-title">First 25 Customers Each Day</span>
      <span class="early-bird-sub">Will Receive a Surprise Gift Valued at $50+</span>
    </section>

    <div class="winter-scene" role="img" aria-label="Misty grey winter forest above a snowy hill"></div>
    <div class="gift-boxes" role="img" aria-label="Wrapped red and white gift boxes with bows and pine sprigs in the snow"></div>

    <p class="centered perks">Tons of Giveaways, Food &amp; Drinks!<br>Bring/Buy an Unopened Toy for Marshgate<br>Kin Aid &amp; Receive a $10 Gift Card.</p>

    <address class="shop-info">
      VELVET CRADLE<br>
      BLUFFTON, SC<br>
      OAKRIDGE PLAZA : NEXT TO PINE GRILL
      <span class="shop-phone">(555) 214-7093</span>
      <span class="social-row">
        <span class="social-dot"></span>
        <span class="social-dot"></span>
        <span class="social-dot"></span>
        <span class="social-dot"></span>
      </span>
    </address>
  </main>
</body>
</html>
```